Halvorsen Electric service department flyer

Looking to design a electrical service department flyer. The company has been in San Francisco for 60yrs primarily doing work in the downtown area. https://halvorsenelectric.example/about-halvorsen/
I attached a rough draft of the flyer. I would like to see something with the san francisco downtown skyline watermarked on the front page, open to the second page that describes all services and contact.

```html
<!DOCTYPE html>
<html lang="en">
<head>
<meta charset="utf-8">
<title>Halvorsen Electric – Service Department Flyer</title>
<link rel="stylesheet" href="https://fonts.googleapis.com/css2?family=Montserrat:wght@500;600;700;800&display=swap">
<style>
  :root {
    --backdrop: #dcdcdc;
    --page-bg: #e3f2fd;
    --line-blue: #1e96e8;
    --heading-blue: #1a8fe0;
    --deep-blue: #0d47a1;
    --footer-blue: #0b4aa8;
    --footer-black: #141414;
    --ink: #1c1c24;
    --white: #ffffff;
  }
  * { box-sizing: border-box; margin: 0; padding: 0; }
  html, body { width: 1200px; height: 1200px; overflow: hidden; }
  body {
    background: var(--backdrop);
    font-family: "Montserrat", Arial, sans-serif;
    color: var(--ink);
    position: relative;
  }
  .page {
    position: absolute;
    top: 203px;
    width: 560px;
    height: 793px;
    background: var(--page-bg);
    overflow: hidden;
    box-shadow: 0 6px 18px rgba(0,0,0,0.18);
  }
  .page--front { left: 26px; }
  .page--inside { left: 614px; }

  .skyline {
    position: absolute; left: 0; top: 0; width: 560px; height: 160px;
    background:
      linear-gradient(180deg, #3a3f78 0%, #8a5a8e 22%, #e0787a 34%, #6a5c8c 46%, #2c3463 62%, #1d2244 100%);
  }
  .brand {
    position: absolute; left: 52px; top: 52px;
    display: flex; align-items: center; gap: 8px;
  }
  .brand__mark { width: 14px; height: 14px; background: var(--white); }
  .brand__name {
    font-weight: 800; font-size: 20px; color: var(--white); letter-spacing: 0.5px;
  }

  .panel {
    position: absolute; left: 28px; width: 291px;
    border: 3px solid var(--line-blue); border-radius: 8px;
    padding: 12px 14px;
  }
  .panel__title {
    font-size: 11px; font-weight: 700; color: var(--heading-blue);
    text-transform: uppercase; margin-bottom: 6px; line-height: 1.25;
  }
  .list { list-style: none; }
  .list li {
    display: flex; align-items: center; gap: 5px;
    font-size: 10px; font-weight: 600; line-height: 17px;
  }
  .list .indent { padding-left: 14px; }
  .icon { width: 9px; height: 9px; flex: none; fill: var(--heading-blue); }
  .icon--line { fill: none; stroke: var(--heading-blue); stroke-width: 1.6; }

  .intro { font-size: 10px; font-weight: 600; line-height: 15px; }
  .services-title {
    font-size: 18px; font-weight: 700; color: var(--deep-blue);
    text-transform: uppercase; line-height: 1;
  }
  .free-estimates {
    position: absolute; left: 42px; top: 505px;
    font-size: 11px; font-weight: 700; color: var(--deep-blue); text-transform: uppercase;
  }

  .photo-rail {
    position: absolute; left: 350px; top: 210px; width: 104px; height: 454px;
    border: 3px solid var(--line-blue); border-radius: 8px;
  }
  .photo {
    position: absolute; left: 377px; width: 150px; height: 150px;
    border-radius: 50%; border: 5px solid var(--white);
    box-shadow: 0 0 0 1px #c9d6e2;
  }
  .photo--lounge { top: 234px; background: radial-gradient(circle at 45% 45%, #e8c370 0%, #9a6a2a 45%, #3a2a1c 100%); }
  .photo--corridor { top: 363px; background: linear-gradient(90deg, #5a3c14 0%, #e6b04a 30%, #2a2420 55%, #1c1a1a 100%); }
  .photo--lobby { top: 485px; background: linear-gradient(180deg, #9a9c9e 0%, #6e7276 50%, #8a8e92 100%); }

  .footer {
    position: absolute; left: 0; top: 712px; width: 560px; height: 56px;
    background: var(--footer-blue); color: var(--white);
    display: flex; align-items: center; justify-content: space-between;
    padding: 0 26px; font-size: 10.5px; font-weight: 500;
  }
  .footer__item { display: flex; align-items: center; gap: 5px; line-height: 15px; }
  .footer .icon { fill: var(--white); }
  .footer-base {
    position: absolute; left: 0; top: 768px; width: 560px; height: 25px;
    background: var(--footer-black);
  }
</style>
</head>
<body>

<svg width="0" height="0" style="position:absolute" aria-hidden="true">
  <defs>
    <symbol id="i-tick" viewBox="0 0 10 10"><circle cx="5" cy="5" r="4.2" fill="none" stroke="currentColor" stroke-width="1"/><path d="M3 5.2 4.5 6.6 7.2 3.6" fill="none" stroke="currentColor" stroke-width="1"/></symbol>
    <symbol id="i-gear" viewBox="0 0 10 10"><path d="M4.2 0h1.6l.3 1.5 1.3.6 1.3-.9 1.1 1.1-.9 1.3.6 1.3 1.5.3v1.6l-1.5.3-.6 1.3.9 1.3-1.1 1.1-1.3-.9-1.3.6-.3 1.5H4.2l-.3-1.5-1.3-.6-1.3.9-1.1-1.1.9-1.3-.6-1.3L0 5.8V4.2l1.5-.3.6-1.3-.9-1.3 1.1-1.1 1.3.9 1.3-.6z"/><circle cx="5" cy="5" r="1.6" fill="#e3f2fd"/></symbol>
    <symbol id="i-phone" viewBox="0 0 10 10"><rect x="0" y="0" width="10" height="10" rx="2"/><path d="M3 2.2 4.2 3.4 3.6 4.2a4 4 0 0 0 2.2 2.2l.8-.6 1.2 1.2-.8.9C4.6 7.8 2.2 5.4 2.1 3z" fill="#e3f2fd"/></symbol>
    <symbol id="i-mail" viewBox="0 0 10 10"><rect x="0" y="0" width="10" height="10" rx="2"/><path d="M2 3h6v4H2z M2 3l3 2.2L8 3" fill="none" stroke="#e3f2fd" stroke-width="0.9"/></symbol>
    <symbol id="i-globe" viewBox="0 0 10 10"><circle cx="5" cy="5" r="4.3" fill="none" stroke="currentColor" stroke-width="1"/><path d="M.7 5h8.6M5 .7c-2.4 2.6-2.4 6 0 8.6M5 .7c2.4 2.6 2.4 6 0 8.6" fill="none" stroke="currentColor" stroke-width="0.9"/></symbol>
    <symbol id="i-pin" viewBox="0 0 10 10"><path d="M5 0a3.6 3.6 0 0 1 3.6 3.6C8.6 6.3 5 10 5 10S1.4 6.3 1.4 3.6A3.6 3.6 0 0 1 5 0zm0 2.2a1.4 1.4 0 1 0 0 2.8 1.4 1.4 0 0 0 0-2.8z"/></symbol>
    <symbol id="i-clock" viewBox="0 0 10 10"><circle cx="5" cy="5" r="5"/><path d="M5 2.3V5l2 1.2" fill="none" stroke="#e3f2fd" stroke-width="1"/></symbol>
  </defs>
</svg>

<!-- Front page -->
<section class="page page--front">
  <div class="skyline" role="img" aria-label="San Francisco downtown skyline at sunset"></div>
  <div class="brand"><span class="brand__mark"></span><span class="brand__name">HALVORSEN ELECTRIC</span></div>

  <div class="panel" style="top:187px;height:109px">
    <h2 class="panel__title">Why choose us</h2>
    <ul class="list" style="color:var(--heading-blue)">
      <li><svg class="icon"><use href="#i-tick"/></svg><span style="color:var(--ink)">Customer service is our priority</span></li>
      <li><svg class="icon"><use href="#i-tick"/></svg><span style="color:var(--ink)">Honest pricing &amp; dependable results</span></li>
      <li><svg class="icon"><use href="#i-tick"/></svg><span style="color:var(--ink)">San Francisco based company since 1966</span></li>
      <li><svg class="icon"><use href="#i-tick"/></svg><span style="color:var(--ink)">Professional, clean and efficient work</span></li>
    </ul>
  </div>

  <div class="panel" style="top:323px;height:155px;color:var(--heading-blue)">
    <h2 class="panel__title">Contact us</h2>
    <ul class="list">
      <li><svg class="icon"><use href="#i-phone"/></svg><span style="color:var(--ink)">(415-555-0142)</span></li>
      <li><svg class="icon"><use href="#i-mail"/></svg><span style="color:var(--ink)">tnordqvist@halvorsenelectric.example</span></li>
      <li><svg class="icon"><use href="#i-globe"/></svg><span style="color:var(--ink)">www.halvorsenelectric.example</span></li>
      <li><svg class="icon"><use href="#i-pin"/></svg><span style="color:var(--ink)">218 Fenwick Street, San Francisco,</span></li>
      <li class="indent"><span style="color:var(--ink)">CA 94103</span></li>
      <li><svg class="icon"><use href="#i-clock"/></svg><span style="color:var(--ink)">Mon-Fri: 8:00 AM - 5:00 PM</span></li>
    </ul>
  </div>

  <p class="free-estimates">Free estimates available</p>

  <div class="panel" style="top:533px;height:163px">
    <h2 class="panel__title">Residential commercial 24/7<br>emergency service</h2>
    <ul class="list">
      <li><svg class="icon"><use href="#i-gear"/></svg>Electrical Repairs</li>
      <li><svg class="icon"><use href="#i-gear"/></svg>Panel Upgrades</li>
      <li><svg class="icon"><use href="#i-gear"/></svg>TI Upgrades</li>
      <li><svg class="icon"><use href="#i-gear"/></svg>Lighting Installation</li>
      <li><svg class="icon"><use href="#i-gear"/></svg>Building maintenance / 24/7 Service</li>
      <li><svg class="icon"><use href="#i-gear"/></svg>EV Charger Installation</li>
    </ul>
  </div>

  <div class="photo-rail"></div>
  <div class="photo photo--lounge" role="img" aria-label="Warmly lit restaurant lounge with pendant lighting"></div>
  <div class="photo photo--corridor" role="img" aria-label="Corridor with golden wall lighting and mailboxes"></div>
  <div class="photo photo--lobby" role="img" aria-label="Bright modern lobby with seating"></div>

  <footer class="footer">
    <div class="footer__item"><svg class="icon"><use href="#i-pin"/></svg><span>218 Fenwick Street<br>San Francisco, CA 94103</span></div>
    <div class="footer__item"><svg class="icon"><use href="#i-mail"/></svg><span>info@halvorsenelectric.example</span></div>
    <div class="footer__item"><svg class="icon"><use href="#i-phone"/></svg><span>415-555-0142</span></div>
  </footer>
  <div class="footer-base"></div>
</section>

<!-- Inside page -->
<section class="page page--inside">
  <div class="skyline" role="img" aria-label="San Francisco downtown skyline at sunset"></div>
  <div class="brand"><span class="brand__mark"></span><span class="brand__name">HALVORSEN ELECTRIC</span></div>

  <div class="panel" style="top:178px;height:109px">
    <p class="intro">Halvorsen Electric is a licensed electrical contractor proudly serving San Francisco and surrounding Bay Area communities. Our experienced electricians provide safe, efficient, and code- compliant electrical solutions for residential and commercial properties.</p>
  </div>

  <div class="panel" style="top:308px;height:38px;padding:8px 14px">
    <h2 class="services-title">Our services</h2>
  </div>

  <div class="panel" style="top:366px;height:156px">
    <h2 class="panel__title">Residential electrical</h2>
    <ul class="list">
      <li><svg class="icon"><use href="#i-gear"/></svg>Electrical repairs &amp; troubleshooting</li>
      <li><svg class="icon"><use href="#i-gear"/></svg>Panel upgrades &amp; breaker replacement</li>
      <li><svg class="icon"><use href="#i-gear"/></svg>Lighting installation (indoor &amp; outdoor)</li>
      <li><svg class="icon"><use href="#i-gear"/></svg>EV charger installation</li>
      <li><svg class="icon"><use href="#i-gear"/></svg>Rewiring &amp; remodels</li>
      <li><svg class="icon"><use href="#i-gear"/></svg>Emergency electrical services</li>
    </ul>
  </div>

  <div class="panel" style="top:546px;height:143px">
    <h2 class="panel__title">Commercial electrical</h2>
    <ul class="list">
      <li><svg class="icon"><use href="#i-gear"/></svg>Office &amp; retail electrical systems</li>
      <li><svg class="icon"><use href="#i-gear"/></svg>Lighting upgrades &amp; maintenance</li>
      <li><svg class="icon"><use href="#i-gear"/></svg>Electrical inspections</li>
      <li><svg class="icon"><use href="#i-gear"/></svg>Tenant improvements</li>
      <li><svg class="icon"><use href="#i-gear"/></svg>Emergency electrical services</li>
    </ul>
  </div>

  <div class="photo-rail" style="top:208px"></div>
  <div class="photo photo--lounge" role="img" aria-label="Warmly lit restaurant lounge with pendant lighting"></div>
  <div class="photo photo--corridor" role="img" aria-label="Corridor with golden wall lighting and mailboxes"></div>
  <div class="photo photo--lobby" role="img" aria-label="Bright modern lobby with seating"></div>

  <footer class="footer">
    <div class="footer__item"><svg class="icon"><use href="#i-pin"/></svg><span>218 Fenwick Street<br>San Francisco, CA 94103</span></div>
    <div class="footer__item"><svg class="icon"><use href="#i-mail"/></svg><span>info@halvorsenelectric.example</span></div>
    <div class="footer__item"><svg class="icon"><use href="#i-phone"/></svg><span>415-555-0142</span></div>
  </footer>
  <div class="footer-base"></div>
</section>

</body>
</html>
```